BrambleWorks business card

Looking for business card design that supports our company/software values. We have 2 logo designs at the moment but open to change if you think you can enhance the brand. Check out website www.brambleworks.com.au.

Target Market(s)

Education

Contact Information for Business Card

Name, title, mobile, email and website

Font styles to use
Sans Serif

Colors

Designer to choose colors to be used in the design.

Requirements
Must have
• BrambleWorks logo with tree and tagline on rear side with dark grey background colour

```html
<!DOCTYPE html>
<html lang="en">
<head>
<meta charset="utf-8">
<title>BrambleWorks business card</title>
<link href="https://fonts.googleapis.com/css2?family=Open+Sans:wght@400;600;700&display=swap" rel="stylesheet">
<style>
  :root {
    --backdrop: #bdbdbd;
    --card-light: #ffffff;
    --card-dark: #141414;
    --accent: #fbb632;
    --ink: #4a4a4a;
    --ink-soft: #333333;
    --mark-grey: #5a5a5a;
    --rule-grey: #4d4d4d;
  }
  * { margin: 0; padding: 0; box-sizing: border-box; }
  html, body {
    width: 1200px; height: 882px; overflow: hidden;
    background: var(--backdrop);
    font-family: "Open Sans", sans-serif;
  }
  .stage {
    width: 1200px; height: 882px;
    display: flex; align-items: center; justify-content: center; gap: 56px;
  }
  .card {
    width: 520px; height: 298px; position: relative;
    box-shadow: 0 10px 24px rgba(0,0,0,0.25);
  }
  .card--front { background: var(--card-light); }
  .card--back { background: var(--card-dark); }

  .front-brand {
    position: absolute; left: 38px; top: 108px;
    display: flex; align-items: center; gap: 10px;
  }
  .front-brand__dot {
    width: 22px; height: 22px; border-radius: 50%; background: var(--accent);
  }
  .front-brand__name {
    font-size: 24px; font-weight: 600; color: var(--ink);
  }

  .contact {
    position: absolute; left: 262px; top: 46px;
  }
  .contact__name {
    font-size: 19px; font-weight: 700; color: var(--accent);
    letter-spacing: 0.5px; line-height: 1.1;
  }
  .contact__title {
    font-size: 13px; color: var(--ink); margin-top: 2px;
  }
  .contact__list { list-style: none; margin-top: 16px; }
  .contact__item {
    display: flex; align-items: center; gap: 9px;
    font-size: 12px; color: var(--ink-soft); line-height: 20px;
  }
  .contact__icon { width: 11px; height: 11px; flex: none; }

  .address {
    position: absolute; left: 38px; bottom: 24px;
    font-size: 12px; color: var(--ink-soft);
  }

  .back-brand {
    position: absolute; left: 0; right: 0; top: 104px;
    display: flex; flex-direction: column; align-items: center;
  }
  .back-brand__name {
    font-size: 50px; font-weight: 600; color: var(--mark-grey);
    letter-spacing: 1px; line-height: 1;
  }
  .back-brand__rule {
    width: 330px; height: 2px; background: var(--rule-grey); margin: 10px 0 6px;
  }
  .back-brand__tagline {
    font-size: 17px; color: var(--mark-grey); letter-spacing: 0.5px;
  }
</style>
</head>
<body>
<main class="stage">
  <section class="card card--front" aria-label="Business card front">
    <div class="front-brand">
      <span class="front-brand__dot"></span>
      <span class="front-brand__name">BrambleWorks</span>
    </div>

    <div class="contact">
      <h1 class="contact__name">DANIEL REYES</h1>
      <p class="contact__title">Founder &amp; CEO</p>
      <ul class="contact__list">
        <li class="contact__item">
          <svg class="contact__icon" viewBox="0 0 12 12"><rect x="3" y="0.5" width="6" height="11" rx="1" fill="none" stroke="#fbb632" stroke-width="1.4"/></svg>
          +43 660 48213957
        </li>
        <li class="contact__item">
          <svg class="contact__icon" viewBox="0 0 12 12"><path d="M2 1.5 L4.5 1.5 L5.5 4 L4 5 Q5 7.5 7 8 L8 6.5 L10.5 7.5 L10.5 10 Q5 10.5 2 5 Z" fill="#fbb632"/></svg>
          +43 660 48213957
        </li>
        <li class="contact__item">
          <svg class="contact__icon" viewBox="0 0 12 12"><rect x="0.5" y="2" width="11" height="8" fill="#fbb632"/><path d="M0.5 2 L6 6.5 L11.5 2" fill="none" stroke="#fff" stroke-width="1"/></svg>
          info@brambleworks.com.au
        </li>
        <li class="contact__item">
          <svg class="contact__icon" viewBox="0 0 12 12"><circle cx="6" cy="6" r="5.5" fill="#fbb632"/><path d="M0.5 6 H11.5 M6 0.5 Q3 6 6 11.5 M6 0.5 Q9 6 6 11.5" fill="none" stroke="#fff" stroke-width="0.8"/></svg>
          www.brambleworks.com.au
        </li>
      </ul>
    </div>

    <p class="address">4400-512 Harbour Lane, Vancouver, BC, V6B 3K7</p>
  </section>

  <section class="card card--back" aria-label="Business card back">
    <div class="back-brand">
      <span class="back-brand__name">BrambleWorks</span>
      <span class="back-brand__rule"></span>
      <span class="back-brand__tagline">Student Success Platform</span>
    </div>
  </section>
</main>
</body>
</html>
```